Coffee bag + cups: retail packaging

Our is seeking new packaging for a new coffee shop concept. As part of this we need to design new packaging for our coffee products. For this request, we are seeking design layouts for our retail bags and a cup for to-go coffee. We are working with 3 logo versions (pending final approval).

Please reference this website to see the types of coffee bag packaging options, there's a variety of bag options. We'd like the bag to be a Gusseted Bag, size 3.625 x 9.6 x 2.3125. We want a matte laminated material, not shiny.
https://www.brellumpack.com/

BAG
We'd like to see options of a black bag, blue, and kraft paper. Reference attached example.

Below is the text for our current bags, you can use that for now. I've attached example of bags that I like. We will look to you for design thoughts.

[Front]
Logo
100% Tanzanian
12oz
Dark Roast
Ground

[Back]
Amber Ridge Farms was established in 1989 by Marcus Ellery, son of baseball legend Thomas Ellery, and his family in rural Tanzania.
Today the coffee brand is sourced exclusively from the Ellery farm and other small scale family owned farms in Tanzania and East Africa.
This international coffee initiative is designed to bring a greater share of coffee revenues to farmers through direct trade and help develop rural communities in East Africa.

Visit us at Kelvorabeans.com

[Left panel]

Brewing instructions: Lorem ipsum dolor sit amet, consectetur adipiscing elit, sed do eiusmod tempor incididunt ut labore et dolore magna aliqua.

[Right panel]

Leave blank

Cup Sleeve
[Front of sleeve]
Logo

To-go cup
[Front]
Logo

Target Market(s)

Specialty coffee lovers.

Font styles to use
Serif
Sans Serif

Colors

Designer to choose colors to be used in the design.

Requirements
Must have
• Examples of coffee bag packaging.
• Must have; logo, text, clear and elegant labeling. Simple but strong.

```html
<!DOCTYPE html>
<html lang="en">
<head>
<meta charset="utf-8">
<title>Amber Ridge Coffee – Gusseted Bag Layout</title>
<link rel="stylesheet" href="https://fonts.googleapis.com/css2?family=Antonio:wght@300;400&family=Oswald:wght@500;600&display=swap">
<style>
  :root {
    --navy: #142a5a;
    --leaf-tint: #2c4a94;
    --gold: #a97f55;
    --frame-gold: #b9936a;
    --brown: #5a2a0c;
    --cream: #fdfbf8;
    --white: #ffffff;
    --muted: #8d9cc2;
    --page: #ffffff;
  }
  * { box-sizing: border-box; margin: 0; padding: 0; }
  html, body { width: 1200px; height: 1000px; overflow: hidden; background: var(--page); }
  .canvas { position: relative; width: 1200px; height: 1000px; }

  .panel { position: absolute; top: 131px; height: 758px; background: var(--navy); overflow: hidden; }
  .panel--back  { left: 69px;  width: 417px; }
  .panel--side  { left: 501px; width: 201px; }
  .panel--front { left: 717px; width: 417px; }

  .botanical { position: absolute; opacity: .55; }
  .botanical--back-top   { left: 120px; top: 0; width: 297px; height: 230px;
    background: radial-gradient(ellipse at 70% 35%, var(--leaf-tint) 0%, rgba(44,74,148,.35) 45%, rgba(20,42,90,0) 75%); }
  .botanical--back-low   { left: 0; top: 520px; width: 120px; height: 238px;
    background: radial-gradient(ellipse at 20% 60%, var(--leaf-tint) 0%, rgba(44,74,148,.3) 45%, rgba(20,42,90,0) 75%); }
  .botanical--front-top  { left: 60px; top: 0; width: 357px; height: 240px;
    background: radial-gradient(ellipse at 65% 35%, var(--leaf-tint) 0%, rgba(44,74,148,.35) 45%, rgba(20,42,90,0) 75%); }
  .botanical--front-low  { left: 0; top: 460px; width: 190px; height: 298px;
    background: radial-gradient(ellipse at 35% 50%, var(--leaf-tint) 0%, rgba(44,74,148,.3) 45%, rgba(20,42,90,0) 75%); }

  .brand-mark { position: absolute; border-radius: 50%; background: var(--cream);
    border: 5px solid var(--brown); display: flex; align-items: center; justify-content: center;
    text-align: center; font-family: "Oswald", sans-serif; font-weight: 600; color: var(--brown);
    text-transform: uppercase; letter-spacing: .14em; line-height: 1.25; }
  .brand-mark--back  { left: 134px; top: 94px;  width: 180px; height: 180px; font-size: 19px; }
  .brand-mark--side  { left: 60px;  top: 618px; width: 82px;  height: 82px;  font-size: 9px; border-width: 3px; }
  .brand-mark--front { left: 98px;  top: 129px; width: 220px; height: 220px; font-size: 24px; border-width: 6px; }

  .story { position: absolute; left: 44px; top: 321px; width: 334px; height: 397px;
    border: 2px solid var(--frame-gold); padding: 28px 0 0 20px; }
  .story__text { font-family: "Antonio", sans-serif; font-weight: 400; font-size: 15.5px;
    line-height: 26px; color: var(--white); letter-spacing: .02em; }
  .story__link { margin-top: 30px; font-family: "Oswald", sans-serif; font-weight: 500;
    font-size: 18px; color: var(--white); text-transform: uppercase; }

  .brewing { position: absolute; left: 38px; top: 356px; width: 140px;
    font-family: "Antonio", sans-serif; font-weight: 300; font-size: 13px; line-height: 22px;
    color: var(--muted); text-transform: uppercase; letter-spacing: .02em; }

  .origin { position: absolute; left: 0; width: 100%; top: 395px; text-align: center;
    font-family: "Oswald", sans-serif; font-weight: 500; font-size: 39px; color: var(--white); }
  .roast { position: absolute; left: 0; width: 100%; top: 500px; text-align: center;
    font-family: "Oswald", sans-serif; font-weight: 500; font-size: 51px; line-height: 56px;
    color: var(--gold); text-transform: uppercase; }
  .weight { position: absolute; left: 0; width: 100%; top: 705px; text-align: center;
    font-family: "Oswald", sans-serif; font-weight: 500; font-size: 20px; color: var(--white); }
</style>
</head>
<body>
<main class="canvas">

  <section class="panel panel--back" aria-label="Back panel">
    <div class="botanical botanical--back-top" role="img" aria-label="Line illustration of coffee branches with leaves and cherries"></div>
    <div class="botanical botanical--back-low" role="img" aria-label="Line illustration of coffee leaves and cherries"></div>
    <div class="brand-mark brand-mark--back">Amber Ridge<br>Coffee</div>
    <div class="story">
      <p class="story__text">Amber Ridge Farms was established in 1989 by Marcus Ellery, son of baseball legend Thomas Ellery, and his family in rural Tanzania. Today the coffee brand is sourced exclusively from the Ellery farm and other small scale family owned farms in Tanzania and East Africa. This international coffee initiative is designed to bring a greater share of coffee revenues to farmers through direct trade and help develop rural communities in East Africa.</p>
      <p class="story__link">Visit us at Kelvorabeans.com</p>
    </div>
  </section>

  <section class="panel panel--side" aria-label="Side panel">
    <p class="brewing">Brewing instructions: Lorem ipsum dolor sit amet, consectetur adipiscing elit, sed do eiusmod tempor incididunt ut labore et dolore magna aliqua.</p>
    <div class="brand-mark brand-mark--side">Amber Ridge<br>Coffee</div>
  </section>

  <section class="panel panel--front" aria-label="Front panel">
    <div class="botanical botanical--front-top" role="img" aria-label="Line illustration of coffee branches with leaves and cherries"></div>
    <div class="botanical botanical--front-low" role="img" aria-label="Line illustration of coffee leaves and cherries"></div>
    <div class="brand-mark brand-mark--front">Amber Ridge<br>Coffee</div>
    <h1 class="origin">100% TANZANIAN</h1>
    <h2 class="roast">Dark Roast<br>Ground</h2>
    <p class="weight">NET WT 12 OZ</p>
  </section>

</main>
</body>
</html>
```